ecommerce news podcast artwork

Podcast cover art for a podcast featuring daily news and events around ecommerce product businesses.

text to be: VORLA BEAT
optional third line of text with smaller font: Podcast

looking for something that pops with a medium to light blue background. text can be in white/red/orange colors. prefer solid colors for text, but background can vary.
I'm really open to other ideas too, sometimes you don't know what you want until you see it.

Target Market(s)

ecommerce business owners, managers

Industry/Entity Type

news, business, ecommerce

Font styles to use
Sans Serif

Colors
0054AA
0677BA
7BADD7
CADEEF
E8F1F8
0094D4
00A9DD
6FCCEA
C7EBF8
E9F6FB
F0912C
F2A743
F7CA91
FBE8D2
FDF5EE
EB3D1F
EC4F4E
F09395
F8D3D4
FCEDEE

Requirements
Must have
• text: VORLA BEAT
Should not have
• no microphones, headsets/headphones, speakers, or other props like that.

```html
<!DOCTYPE html>
<html lang="en">
<head>
<meta charset="utf-8">
<title>Vorla Beat Podcast – Cover Art</title>
<link rel="stylesheet" href="https://fonts.googleapis.com/css2?family=Unbounded:wght@800;900&display=swap">
<style>
  :root {
    --stage: #d9d9d9;
    --orange-deep: #f08a1c;
    --orange-mid: #f2a743;
    --orange-light: #f7b860;
    --cream: #fbe8d2;
    --label-ink: #f0912c;
    --cart-teal: #7cc4b4;
    --bag-pastel: #f7ca91;
  }
  * { margin: 0; padding: 0; box-sizing: border-box; }
  html, body {
    width: 1200px;
    height: 675px;
    overflow: hidden;
    background: var(--stage);
  }
  .stage {
    position: relative;
    width: 1200px;
    height: 675px;
    display: flex;
    align-items: center;
    justify-content: center;
  }
  .cover-art {
    width: 607px;
    height: 607px;
    display: block;
  }
  .cover-title {
    font-family: "Unbounded", "Arial Black", sans-serif;
    font-weight: 900;
    fill: var(--cream);
  }
  .cover-label {
    font-family: "Unbounded", "Arial Black", sans-serif;
    font-weight: 900;
    fill: var(--label-ink);
    letter-spacing: 0.5px;
  }
  .title-frame {
    fill: none;
    stroke: var(--cream);
    stroke-width: 3;
  }
  .label-box { fill: var(--cream); }
</style>
</head>
<body>
<main class="stage">
  <svg class="cover-art" viewBox="0 0 607 607" xmlns="http://www.w3.org/2000/svg" aria-labelledby="cover-title">
    <title id="cover-title">Vorla Beat Podcast</title>
    <defs>
      <radialGradient id="bg-glow" cx="0.35" cy="0.7" r="0.85">
        <stop offset="0" stop-color="var(--orange-light)"/>
        <stop offset="0.55" stop-color="var(--orange-mid)"/>
        <stop offset="1" stop-color="var(--orange-deep)"/>
      </radialGradient>
      <linearGradient id="cart-tone" x1="0" y1="0" x2="1" y2="1">
        <stop offset="0" stop-color="var(--bag-pastel)"/>
        <stop offset="0.6" stop-color="var(--cart-teal)" stop-opacity="0.75"/>
        <stop offset="1" stop-color="var(--orange-mid)" stop-opacity="0"/>
      </linearGradient>
    </defs>

    <rect class="cover-bg" width="607" height="607" fill="url(#bg-glow)"/>

    <rect class="title-frame" x="27" y="26" width="555" height="229"/>

    <text class="cover-title" x="61" y="127" font-size="120" textLength="482" lengthAdjust="spacingAndGlyphs">VORLA</text>
    <text class="cover-title" x="47" y="221" font-size="120" textLength="513" lengthAdjust="spacingAndGlyphs">BEAT</text>

    <rect class="label-box" x="234" y="240" width="140" height="25"/>
    <text class="cover-label" x="304" y="260" font-size="18" text-anchor="middle" textLength="122" lengthAdjust="spacingAndGlyphs">PODCAST</text>

    <rect class="cart-photo" role="img" aria-label="Photo of a small mint-green shopping cart filled with pastel paper shopping bags"
          x="174" y="291" width="278" height="297" rx="40" fill="url(#cart-tone)"/>
  </svg>
</main>
</body>
</html>
```